Yard Nest+ - Outdoors Home Improvents, Upkeeing and Maintenance services

I need a website that looks environmental and refreshing. Yard Nest+ is a home upkeeping services and maintenance for all seasons. I will need a website that can create the feel or atmosphere of each season in separate tabs (ie for summer design should illustrate lawn mowing and gardening services etc while the winter would illustrate snow shovelling services likewise for fall illustratating leaves raking services. Each service should have there own feel to it as if the pages/tab was solely dedicated to that service. Four services in total winter, fall, spring, summer and would like it to have a fun and engaging feel to it with rollover images and links to service description pages.
Updates

Sorry name of the company is brook lanes can you revise the name. I will add a picture to the brief you can get the logo from Added Thursday, April 14, 2016

Target Market(s)

Home Owners, rental suites, landlords, real estate commercial/residential

Industry/Entity Type

Home Improvement

Number of Pages Required

4 page

Font styles to use
Serif
Decorative
Script

Colors
33b8a4
add136
fbee3d
ffffff
ec1f27
ffc214
f37122
f78f20
1b1b1b

Requirements
Must have
• Each service should have there own feel to it as if the pages/tab was solely dedicated to that service. Four services in total winter, fall, spring, summer and would like it to have a fun and engaging feel to it with rollover images and links to service description pages.
Nice to have
Should not have
• Dull and unwelcoming

```html
<!DOCTYPE html>
<html lang="en">
<head>
<meta charset="utf-8">
<title>Brook Lanes — Outdoor Upkeep Services</title>
<link href="https://fonts.googleapis.com/css2?family=Oswald:wght@400;500;600&family=Open+Sans:wght@400;600;700&display=swap" rel="stylesheet">
<style>
:root{
  --orange:#f78f20;
  --orange-deep:#f37122;
  --teal:#33b8a4;
  --teal-dark:#2a9d8c;
  --green:#add136;
  --ink:#1b1b1b;
  --text:#666;
  --light:#f2f2f2;
  --partner:#b3b3b3;
  --white:#fff;
}
*{box-sizing:border-box;margin:0;padding:0}
html,body{width:1200px;height:2416px;overflow:hidden}
body{font-family:"Open Sans",sans-serif;color:var(--text);background:var(--white);position:relative;font-size:14px;line-height:1.6}
.abs{position:absolute}
h1,h2,h3,.nav a,.tab{font-family:"Oswald",sans-serif}
.accent{color:var(--orange)}

/* top bar */
.topbar{top:0;left:0;width:1200px;height:96px}
.call{left:40px;top:36px;font-size:15px;font-weight:600;color:var(--orange)}
.call b{color:var(--ink);font-weight:600;margin-left:6px}
.contact-right{right:40px;top:28px;display:flex;align-items:center;gap:10px;font-size:15px;font-weight:600;color:var(--orange)}
.contact-right span b{color:var(--ink);font-weight:600;margin-left:4px}
.social{width:34px;height:34px;border-radius:50%;border:2px solid var(--ink)}

/* nav */
.nav{top:96px;left:0;width:1200px;height:40px;background:var(--orange);display:flex;justify-content:space-between;padding:0 60px}
.nav ul{display:flex;list-style:none;gap:38px;align-items:center;height:40px}
.nav a{color:var(--white);text-decoration:none;font-size:15px;letter-spacing:.5px}
.brand{left:490px;top:0;width:220px;height:168px;background:var(--white);border-radius:0 0 16px 16px;box-shadow:0 4px 10px rgba(0,0,0,.15);display:flex;flex-direction:column;align-items:center;justify-content:center;gap:10px;z-index:3}
.brand-dot{width:70px;height:70px;border-radius:50%;background:var(--teal)}
.brand-name{font-family:"Oswald",sans-serif;font-size:24px;font-weight:500;color:var(--ink);letter-spacing:1px}

/* hero */
.hero{top:136px;left:0;width:1200px;height:644px;background:linear-gradient(180deg,#5f7f4a 0%,#6f9a4e 35%,#88b357 60%,#6e9b3f 100%)}
.hero-caption{left:0;top:320px;width:600px;padding:22px 40px;background:rgba(27,27,27,.55);color:var(--white);white-space:nowrap}
.hero-caption h1{font-size:42px;font-weight:500;line-height:1.15}
.hero-caption p{font-family:"Oswald",sans-serif;font-size:26px;line-height:1.3}
.hero-arrows{right:40px;top:600px;display:flex;gap:6px;z-index:3}
.hero-arrows span{width:38px;height:38px;background:rgba(27,27,27,.6);display:flex;align-items:center;justify-content:center}

/* season tabs */
.seasons{top:700px;left:80px;width:1040px;height:120px;display:flex;z-index:2}
.season-photo{width:200px;height:120px}
.tab{width:320px;height:120px;display:flex;align-items:center;justify-content:center;color:var(--white);font-size:36px;position:relative}
.tab.summer{background:var(--teal)}
.tab.summer::after{content:"";position:absolute;left:145px;bottom:-20px;border-left:16px solid transparent;border-right:16px solid transparent;border-top:20px solid var(--teal)}
.tab.winter{background:var(--orange)}

/* welcome */
.welcome{top:860px;left:0;width:1200px;text-align:center}
.welcome h2{font-size:32px;font-weight:500;color:var(--ink)}
.welcome p.lead{width:1040px;margin:14px auto 0;font-size:13px;text-align:left}
.features{top:1050px;left:90px;width:1020px;display:flex;justify-content:space-between}
.feature{width:320px;display:flex;gap:18px}
.feature-icon{flex:none;width:66px;height:66px;border-radius:50%;border:2px solid var(--teal);display:flex;align-items:center;justify-content:center}
.feature h3{font-size:18px;font-weight:500;color:var(--ink);margin-bottom:6px}
.feature p{font-size:12px}

/* projects */
.projects{top:1240px;left:0;width:1200px;height:470px;background:var(--light)}
.section-title{text-align:center;padding-top:46px}
.section-title h2{font-size:32px;font-weight:500;color:var(--ink)}
.section-title p{font-size:13px}
.project-grid{top:150px;left:86px;display:flex;gap:22px}
.project{width:240px}
.project-photo{width:240px;height:150px}
.project h3{font-family:"Oswald",sans-serif;font-size:16px;font-weight:500;color:var(--teal);margin:16px 0 6px}
.project p{font-size:12px}
.more{font-size:12px;color:var(--teal);font-weight:600}

/* news */
.news-head{top:1730px;left:86px;width:1028px;display:flex;justify-content:space-between;align-items:center}
.news-head h2{font-size:28px;font-weight:500;color:var(--ink)}
.news-head svg{margin-left:6px}
.news{top:1790px;left:86px;width:1028px;display:flex;justify-content:space-between}
.news-item{width:490px;display:flex;gap:24px}
.news-photo{flex:none;width:220px;height:160px}
.news-item h3{font-family:"Oswald",sans-serif;font-size:16px;font-weight:500;color:var(--ink);margin:8px 0 8px}
.news-item p{font-size:12px}

/* partners: plain placeholders */
.partners{top:2015px;left:86px;width:1028px;height:60px;display:flex;justify-content:space-between;align-items:center}
.partner{width:130px;height:40px;background:var(--partner);border-radius:4px}

/* footer */
.footer{top:2100px;left:0;width:1200px;height:270px;background:var(--teal);color:var(--white);display:flex;gap:60px;padding:46px 86px 0}
.footer h4{font-family:"Oswald",sans-serif;font-size:16px;font-weight:500;margin-bottom:16px;letter-spacing:.5px}
.footer ul{list-style:none;font-size:12px;line-height:2}
.footer p{font-size:12px;line-height:1.8}
.col-links{width:150px}
.col-testi{width:300px}
.col-touch{width:230px}
.col-follow{width:220px}
.footer .social{border-color:var(--white);display:inline-block;margin-right:8px;margin-top:14px}
.copyright{top:2370px;left:0;width:1200px;height:46px;background:var(--ink);color:#bbb;font-size:12px;display:flex;align-items:center;justify-content:center}
</style>
</head>
<body>

<header class="topbar abs">
  <div class="call abs">CALL US : <b>555 010 2468</b></div>
  <div class="contact-right abs">
    <span>EMAIL : <b>hello@brooklanes.example</b></span>
    <span class="social"></span><span class="social"></span><span class="social"></span>
  </div>
</header>

<div class="brand abs">
  <span class="brand-dot"></span>
  <span class="brand-name">BROOK LANES</span>
</div>

<nav class="nav abs">
  <ul><li><a href="#">HOME</a></li><li><a href="#">ABOUT US</a></li><li><a href="#">SERVICES</a></li><li><a href="#">PROJECTS</a></li></ul>
  <ul><li><a href="#">WHAT WE DO</a></li><li><a href="#">BLOG</a></li><li><a href="#">NEWS</a></li><li><a href="#">CONTACTS</a></li></ul>
</nav>

<section class="hero abs" role="img" aria-label="Worker riding a red lawn tractor across a green lawn with trees and hedges behind">
  <div class="hero-caption abs">
    <h1>HOME UP KEEPING SERVICES</h1>
    <p>Outdoor improvements and maintenance</p>
  </div>
  <div class="hero-arrows abs">
    <span><svg width="12" height="16" viewBox="0 0 12 16"><path d="M9 2 3 8l6 6" stroke="#fff" stroke-width="2.5" fill="none"/></svg></span>
    <span><svg width="12" height="16" viewBox="0 0 12 16"><path d="M3 2l6 6-6 6" stroke="#fff" stroke-width="2.5" fill="none"/></svg></span>
  </div>
</section>

<div class="seasons abs">
  <div class="season-photo" role="img" aria-label="Red lawn mower on fresh cut grass" style="background:linear-gradient(135deg,#8fb35a,#c0463e 60%,#6f9a4e)"></div>
  <div class="tab summer">SUMMER</div>
  <div class="season-photo" role="img" aria-label="House front covered in winter snow" style="background:linear-gradient(135deg,#dfe6ec,#9aa7b3)"></div>
  <div class="tab winter">WINTER</div>
</div>

<section class="welcome abs">
  <h2>WELCOME TO <span class="accent">SUMMER SEASON</span></h2>
  <p class="lead">Our crews keep your yard fresh, green and tidy all summer long. We mow lawns, trim hedges, weed flower beds and water gardens so your outdoor space stays welcoming for family and guests. Each visit is planned around your property, your schedule and the weather, and every job is checked before we leave. Whether you own a home, manage rental suites or look after commercial grounds, our team brings reliable, friendly care to every corner of your lawn and garden this season.</p>
</section>

<div class="features abs">
  <div class="feature">
    <div class="feature-icon"><svg width="30" height="30" viewBox="0 0 30 30"><path d="M4 24h22M8 24V14h12l3 10M12 14V8" stroke="#33b8a4" stroke-width="2" fill="none"/></svg></div>
    <div><h3>Lawn mowing</h3><p>Even, clean cuts every week with edging and clippings cleared from paths and drives.</p></div>
  </div>
  <div class="feature">
    <div class="feature-icon"><svg width="30" height="30" viewBox="0 0 30 30"><path d="M6 24C6 12 14 6 24 6c0 10-6 18-18 18zM6 24 18 12" stroke="#33b8a4" stroke-width="2" fill="none"/></svg></div>
    <div><h3>Gardening services</h3><p>Planting, pruning and weeding to keep beds and borders bright through the warm months.</p></div>
  </div>
  <div class="feature">
    <div class="feature-icon"><svg width="30" height="30" viewBox="0 0 30 30"><circle cx="15" cy="15" r="5" stroke="#33b8a4" stroke-width="2" fill="none"/><path d="M15 3v4M15 23v4M3 15h4M23 15h4M6.5 6.5l3 3M20.5 20.5l3 3M6.5 23.5l3-3M20.5 9.5l3-3" stroke="#33b8a4" stroke-width="2"/></svg></div>
    <div><h3>Summer</h3><p>Seasonal plans with watering, feeding and care that keep lawns healthy in the heat.</p></div>
  </div>
</div>

<section class="projects abs">
  <div class="section-title">
    <h2>OUR <span class="accent">PROJECTS</span></h2>
    <p>Recent yards and gardens our crews have cared for this year</p>
  </div>
  <div class="project-grid abs">
    <article class="project">
      <div class="project-photo" role="img" aria-label="Gardener pushing a mower across a lawn" style="background:linear-gradient(135deg,#7fa84c,#4f7a32)"></div>
      <h3>NEQUE PORRO QUISQUAM</h3>
      <p>Weekly mowing and edging for a family home with a large front lawn.</p>
      <span class="more">Read More »</span>
    </article>
    <article class="project">
      <div class="project-photo" role="img" aria-label="Gardener trimming a hedge beside a path" style="background:linear-gradient(135deg,#9bb872,#5e8541)"></div>
      <h3>NEQUE PORRO QUISQUAM</h3>
      <p>Hedge shaping and bed weeding for a row of rental suites downtown.</p>
      <span class="more">Read More »</span>
    </article>
    <article class="project">
      <div class="project-photo" role="img" aria-label="Worker mowing a wide green lawn" style="background:linear-gradient(135deg,#6f9e3e,#3f6b2a)"></div>
      <h3>NEQUE PORRO QUISQUAM</h3>
      <p>Full season lawn care for an office park with shared green space.</p>
      <span class="more">Read More »</span>
    </article>
    <article class="project">
      <div class="project-photo" role="img" aria-label="Gardener tending plants in a backyard" style="background:linear-gradient(135deg,#8db35e,#557d3a)"></div>
      <h3>NEQUE PORRO QUISQUAM</h3>
      <p>Garden planting and mulching for a landlord's corner property.</p>
      <span class="more">Read More »</span>
    </article>
  </div>
</section>

<div class="news-head abs">
  <h2>LATEST <span class="accent">NEWS</span></h2>
  <div>
    <svg width="10" height="14" viewBox="0 0 10 14"><path d="M8 1 2 7l6 6" stroke="#1b1b1b" stroke-width="2" fill="none"/></svg>
    <svg width="10" height="14" viewBox="0 0 10 14"><path d="M2 1l6 6-6 6" stroke="#1b1b1b" stroke-width="2" fill="none"/></svg>
  </div>
</div>

<div class="news abs">
  <article class="news-item">
    <div class="news-photo" role="img" aria-label="Gardener mowing a lawn near a house" style="background:linear-gradient(135deg,#86ad55,#4c7631)"></div>
    <div>
      <h3>SIMPLY DUMMY TEXT</h3>
      <p>Our summer schedule is open. Book regular mowing early to secure your preferred weekday, and ask about our garden bundle for new customers this season.</p>
      <span class="more">Read More »</span>
    </div>
  </article>
  <article class="news-item">
    <div class="news-photo" role="img" aria-label="Worker with a push mower on a sunny lawn" style="background:linear-gradient(135deg,#97bb66,#5a8239)"></div>
    <div>
      <h3>SIMPLY DUMMY TEXT</h3>
      <p>Tips for a healthy lawn in hot weather: water early in the morning, cut a little higher and leave short clippings to feed the soil naturally.</p>
      <span class="more">Read More »</span>
    </div>
  </article>
</div>

<div class="partners abs" role="list" aria-label="Partner companies">
  <span class="partner" role="listitem" aria-label="Partner placeholder"></span>
  <span class="partner" role="listitem" aria-label="Partner placeholder"></span>
  <span class="partner" role="listitem" aria-label="Partner placeholder"></span>
  <span class="partner" role="listitem" aria-label="Partner placeholder"></span>
  <span class="partner" role="listitem" aria-label="Partner placeholder"></span>
  <span class="partner" role="listitem" aria-label="Partner placeholder"></span>
</div>

<footer class="footer abs">
  <div class="col-links">
    <h4>LINKS</h4>
    <ul><li>» Who we are</li><li>» How we work</li><li>» Help</li><li>» Pricing</li><li>» Blog</li></ul>
  </div>
  <div class="col-testi">
    <h4>CLIENT'S TESTIMONIALS</h4>
    <p>" The crew arrived on time every week and our lawn has never looked better. Friendly people, fair prices and tidy work from start to finish. "</p>
    <p>— Happy homeowner</p>
  </div>
  <div class="col-touch">
    <h4>GET IN TOUCH</h4>
    <p>Address : 42 Meadow Row,<br>Greenfield, ON<br>Phone : 555 010 2468<br>Email : hello@brooklanes.example</p>
  </div>
  <div class="col-follow">
    <h4>FOLLOW US</h4>
    <p>Connect with our social network</p>
    <span class="social"></span><span class="social"></span><span class="social"></span>
  </div>
</footer>

<div class="copyright abs">Copyright © 2016 . All Rights Reserved</div>

</body>
</html>
```